PowerPoint Corporate Template for Healthcare AI Technology Company

Take logo and create a comprehensive source file for corporate PowerPoint presentation library that provides an array of title/separator slides, graphic presentation options, chart options and text slide options. Utilize the current logo files and provide options on white backgrounds, and knock out options.

Target Market(s)

Pharmaceutical Manufacturers

Font styles to use
Sans Serif

Colors
6b449b
0556a4
33a6d7
0393ce
ffffff
e34197

Requirements
Must have
• Use logos upgraded in files; create an embedded color palette that aligns to the logo; include multiple options for different types of slides including charts; create a bullet point that is the logo in the purple/blue color with white background; incorporate knock out logo version option for separator pages; must include page numbers; use font aligned to logo for text slide options
Nice to have
• Tech looking, data intensive slide options that communicate easily; could be using 3-4 data points per slide
Should not have
• Any logo other than what has been shared

```html
<!DOCTYPE html>
<html lang="en">
<head>
<meta charset="utf-8">
<title>Presentation Deck – Slide Library</title>
<link href="https://fonts.googleapis.com/css2?family=Montserrat:wght@400;500;600;700;800&family=Raleway:wght@300;400;500&display=swap" rel="stylesheet">
<style>
:root{
  --purple:#6b449b;
  --violet:#7b52b0;
  --indigo:#5f6fc2;
  --teal:#1fc0d6;
  --cyan:#33a6d7;
  --ink:#2a2a33;
  --dark:#1f1f25;
  --grey:#8a8a96;
  --line:#e4e4ee;
  --white:#ffffff;
  --grad:linear-gradient(160deg,#6b449b 0%,#5d6cc3 50%,#1fc0d6 100%);
  --grad-h:linear-gradient(90deg,#1fc0d6 0%,#5d6cc3 55%,#6b449b 100%);
}
*{margin:0;padding:0;box-sizing:border-box}
html,body{width:1200px;height:2563px;overflow:hidden;background:#eef0f5}
body{position:relative;font-family:"Montserrat",sans-serif;color:var(--ink)}
.canvas{position:relative;width:1200px;height:2563px;overflow:hidden}

/* hero */
.hero-bg{position:absolute;left:0;top:0;width:1200px;height:495px;background:linear-gradient(180deg,#e3e3ea 0%,#d6d6df 55%,#eeeef3 100%)}
.hero-title{position:absolute;left:70px;top:180px;line-height:1}
.hero-title .a{display:block;font-weight:800;font-size:62px;color:#6a5bc0;letter-spacing:-.5px}
.hero-title .b{display:block;font-weight:400;font-size:62px;color:#1d1d22;margin:4px 0 0 128px}
.hero-slide{position:absolute;left:565px;top:85px;width:470px;height:262px;overflow:hidden;box-shadow:0 12px 30px rgba(40,40,70,.25)}

/* slide base */
.slide{position:absolute;width:386px;height:216px;overflow:hidden;background:var(--white)}
.c1{left:15px}.c2{left:410px}.c3{left:805px}
.abs{position:absolute}
.tab{position:absolute;left:183px;top:0;width:20px;height:8px;background:var(--violet)}
.tab-b{position:absolute;left:183px;bottom:7px;width:20px;height:3px;background:var(--violet)}
.foot-copy{position:absolute;left:18px;bottom:6px;font-size:3.6px;color:var(--grey)}
.foot-num{position:absolute;left:0;right:0;bottom:12px;text-align:center;font-size:3.6px;color:var(--grey)}
.foot-brand{position:absolute;right:16px;bottom:4px;display:flex;align-items:center;gap:2px;font-family:"Raleway",sans-serif;font-weight:300;font-size:8px;color:var(--indigo)}
.foot-brand i{width:6px;height:6px;border:1px solid var(--indigo);border-radius:50%}

.brand{display:flex;align-items:center;gap:5px;font-family:"Raleway",sans-serif;font-weight:300;color:var(--purple)}
.brand i{display:block;border:1.5px solid currentColor;border-radius:50%}
.brand.light{color:#fff}

.ttl{font-family:"Raleway",sans-serif;font-weight:400;font-size:13px;color:var(--ink);text-align:center}
.sub{font-weight:600;font-size:4.6px;letter-spacing:1.6px;color:var(--indigo);text-align:center}
.hdr{position:absolute;left:0;top:0;width:100%;height:62px;background:var(--grad-h);color:#fff;text-align:center;padding-top:18px}
.hdr .ttl{color:#fff;font-size:15px}
.hdr .sub{color:#e9ecff}
.head{position:absolute;left:0;width:100%;top:14px;text-align:center}
.head.left{text-align:left}
.head.left .ttl,.head.left .sub{text-align:left}

.big-ttl{font-weight:700;color:#fff;text-align:center}
.pres{font-size:4.6px;letter-spacing:2px;font-weight:600;text-align:center;color:#fff}
.pres b{display:block;letter-spacing:.5px;font-size:4.4px;margin-top:1px}
.socials{display:flex;gap:3px;justify-content:center}
.socials i{width:7px;height:7px;border:1px solid currentColor;border-radius:50%}

.txt{font-size:4.4px;line-height:1.5;color:#60606c}
.item{position:absolute;width:150px;display:flex;gap:8px}
.item .ico{flex:0 0 14px;height:14px;border:1px solid var(--indigo);border-radius:50%;margin-top:2px}
.item .nm{font-size:5px;font-weight:600;color:var(--indigo);margin-bottom:1px}
.ph{position:absolute}
.card{position:absolute;border-radius:8px;color:#fff;padding:8px}
.card .h{font-size:5.5px;font-weight:700;margin-bottom:3px}
.card .txt{color:#f1f1ff}
.donut-label{position:absolute;font-weight:700;color:var(--ink);text-align:center}
.bul{display:flex;gap:6px;align-items:flex-start;margin-bottom:8px}
.bul i{flex:0 0 8px;height:8px;border:1px solid var(--indigo);border-radius:50%}
</style>
</head>
<body>
<div class="canvas">

<!-- hero -->
<div class="hero-bg" role="img" aria-label="Photograph of friends raising their arms against a sunset sky"></div>
<h1 class="hero-title"><span class="a">Presentation</span><span class="b">Deck</span></h1>
<div class="hero-slide">
  <div class="abs" style="left:0;top:0;width:470px;height:56px;background:#fff;display:flex;justify-content:center;align-items:center">
    <div class="brand" style="font-size:20px"><i style="width:22px;height:22px"></i>Medivant</div>
  </div>
  <div class="abs" style="left:0;top:56px;width:470px;height:206px;background:var(--grad)">
    <div class="big-ttl" style="font-size:17px;margin-top:70px">Prestation Title Goes Here</div>
    <div class="sub" style="color:#fff;margin-top:8px;font-size:5.5px;letter-spacing:2.4px">SUB TITLE GOES HERE</div>
    <div class="pres" style="margin-top:36px;font-size:5.5px">PRESENTED BY<b>Presenter name</b></div>
    <div class="socials" style="color:#fff;margin-top:6px"><i></i><i></i><i></i></div>
  </div>
</div>

<!-- row 1 -->
<section class="slide c1" style="top:500px">
  <div class="abs" style="left:0;top:0;width:386px;height:45px;display:flex;justify-content:center;align-items:center">
    <div class="brand" style="font-size:15px"><i style="width:16px;height:16px"></i>Medivant</div>
  </div>
  <div class="abs" style="left:0;top:45px;width:386px;height:171px;background:var(--grad)">
    <div class="big-ttl" style="font-size:14px;margin-top:58px">Prestation Title Goes Here</div>
    <div class="sub" style="color:#fff;margin-top:5px">SUB TITLE GOES HERE</div>
    <div class="pres" style="margin-top:28px">PRESENTED BY<b>Presenter name</b></div>
    <div class="socials" style="color:#fff;margin-top:4px"><i></i><i></i><i></i></div>
  </div>
</section>

<section class="slide c2" style="top:500px">
  <div class="ph" style="inset:0;background:linear-gradient(135deg,#f3f4f8,#e6e8ef)" role="img" aria-label="Faint photograph of glass building architecture"></div>
  <div class="abs" style="left:183px;top:42px;width:20px;height:20px;border:2px solid var(--indigo);border-radius:50%"></div>
  <div class="abs" style="left:0;top:86px;width:386px;text-align:center;font-weight:700;font-size:14px;color:var(--ink)">Prestation Title Goes Here</div>
  <div class="sub abs" style="left:0;top:108px;width:386px;color:var(--grey)">SUB TITLE GOES HERE</div>
  <div class="abs" style="left:0;top:155px;width:386px;height:61px;background:var(--indigo);padding-top:20px">
    <div class="pres">PRESENTED BY<b>Presenter name</b></div>
  </div>
</section>

<section class="slide c3" style="top:500px">
  <div class="ph" style="left:0;top:0;width:193px;height:216px;background:var(--dark)" role="img" aria-label="Dark circular dot pattern background"></div>
  <div class="abs brand light" style="left:42px;top:98px;font-size:17px;color:#9a8fd8"><i style="width:17px;height:17px"></i>Medivant</div>
  <div class="abs" style="left:193px;top:58px;width:193px;text-align:center;font-weight:700;font-size:14px;line-height:1.3">Prestation Title<br>Goes Here</div>
  <div class="sub abs" style="left:193px;top:100px;width:193px;color:var(--ink)">SUB TITLE GOES HERE</div>
  <div class="pres abs" style="left:193px;top:165px;width:193px;color:var(--ink)">PRESENTED BY<b>Presenter name</b></div>
  <div class="socials abs" style="left:193px;top:193px;width:193px;color:var(--ink)"><i></i><i></i><i></i></div>
</section>

<!-- row 2 -->
<section class="slide c1" style="top:730px;background:var(--dark)">
  <div class="abs brand" style="left:138px;top:44px;font-size:17px;color:#9a8fd8"><i style="width:20px;height:20px"></i>Medivant</div>
  <div class="big-ttl abs" style="left:0;top:96px;width:386px;font-size:14px">Prestation Title Goes Here</div>
  <div class="sub abs" style="left:0;top:118px;width:386px;color:#fff">SUB TITLE GOES HERE</div>
  <div class="pres abs" style="left:0;top:163px;width:386px">PRESENTED BY<b>Presenter name</b></div>
</section>

<section class="slide c2" style="top:730px;background:var(--dark)">
  <div class="abs" style="left:181px;top:36px;width:24px;height:24px;border:2px solid #7f8ee0;border-radius:50%"></div>
  <div class="big-ttl abs" style="left:0;top:98px;width:386px;font-size:14px">Prestation Title Goes Here</div>
  <div class="sub abs" style="left:0;top:120px;width:386px;color:#fff">SUB TITLE GOES HERE</div>
  <div class="pres abs" style="left:0;top:163px;width:386px">PRESENTED BY<b>Presenter name</b></div>
  <div class="socials abs" style="left:0;top:196px;width:386px;color:var(--indigo)"><i></i><i></i><i></i></div>
</section>

<section class="slide c3" style="top:730px;background:linear-gradient(20deg,#6b449b 0%,#4f7fcb 55%,#1fc0d6 100%)">
  <div class="abs" style="left:12px;top:56px;font-weight:700;font-size:44px;color:rgba(255,255,255,.18)">01</div>
  <div class="abs" style="left:34px;top:76px;font-family:'Raleway',sans-serif;font-size:30px;line-height:1;color:#fff">Slide<br>Break</div>
  <p class="txt abs" style="left:34px;top:146px;width:185px;color:#e8eaff">Short summary of this section and the main points that the next slides will cover in detail for the audience.</p>
</section>

<!-- row 3 -->
<section class="slide c1" style="top:960px">
  <div class="hdr"><div class="ttl">Add Awesome Title Here</div><div class="sub">ADD SUBTITLE HERE</div></div>
  <div class="tab" style="background:var(--violet)"></div>
  <div class="item" style="left:28px;top:74px"><i class="ico"></i><div><div class="nm">Project name</div><p class="txt">Short note on the goals and results of this project.</p></div></div>
  <div class="item" style="left:208px;top:74px"><i class="ico"></i><div><div class="nm">Project name</div><p class="txt">Short note on the goals and results of this project.</p></div></div>
  <div class="item" style="left:28px;top:114px"><i class="ico"></i><div><div class="nm">Project name</div><p class="txt">Short note on the goals and results of this project.</p></div></div>
  <div class="item" style="left:208px;top:114px"><i class="ico"></i><div><div class="nm">Project name</div><p class="txt">Short note on the goals and results of this project.</p></div></div>
  <div class="item" style="left:28px;top:154px"><i class="ico"></i><div><div class="nm">Project name</div><p class="txt">Short note on the goals and results of this project.</p></div></div>
  <div class="item" style="left:208px;top:154px"><i class="ico"></i><div><div class="nm">Project name</div><p class="txt">Short note on the goals and results of this project.</p></div></div>
  <div class="tab-b"></div><div class="foot-copy">Copyright © | All Rights Reserved</div><div class="foot-brand"><i></i>Medivant</div>
</section>

<section class="slide c2" style="top:960px">
  <div class="hdr"><div class="ttl">Add Awesome Title Here</div><div class="sub">ADD SUBTITLE HERE</div></div>
  <div class="tab"></div>
  <svg class="abs" style="left:0;top:0" width="386" height="216">
    <line x1="58" y1="131" x2="352" y2="131" stroke="#2a2a33" stroke-width="2"/>
    <circle cx="40" cy="129" r="5" fill="none" stroke="var(--indigo)" stroke-width="1.2"/>
    <g fill="var(--teal)"><circle cx="88" cy="131" r="3"/><circle cx="145" cy="131" r="3"/><circle cx="202" cy="131" r="3"/><circle cx="260" cy="131" r="3"/><circle cx="316" cy="131" r="3"/></g>
  </svg>
  <div class="abs" style="left:78px;top:114px;font-size:6px;font-weight:700;color:var(--purple)">2001</div>
  <div class="abs" style="left:135px;top:140px;font-size:6px;font-weight:700;color:var(--purple)">2019</div>
  <div class="abs" style="left:192px;top:114px;font-size:6px;font-weight:700;color:var(--purple)">2020</div>
  <div class="abs" style="left:250px;top:140px;font-size:6px;font-weight:700;color:var(--purple)">2021</div>
  <div class="abs" style="left:306px;top:114px;font-size:6px;font-weight:700;color:var(--purple)">2022</div>
  <p class="txt abs" style="left:112px;top:88px;width:62px;text-align:center">Key milestone for the team this year.</p>
  <p class="txt abs" style="left:228px;top:88px;width:62px;text-align:center">Key milestone for the team this year.</p>
  <p class="txt abs" style="left:55px;top:142px;width:62px;text-align:center">Key milestone for the team this year.</p>
  <p class="txt abs" style="left:170px;top:142px;width:62px;text-align:center">Key milestone for the team this year.</p>
  <p class="txt abs" style="left:284px;top:142px;width:62px;text-align:center">Key milestone for the team this year.</p>
  <div class="tab-b"></div><div class="foot-copy">Copyright © | All Rights Reserved</div><div class="foot-brand"><i></i>Medivant</div>
</section>

<section class="slide c3" style="top:960px">
  <div class="head"><div class="ttl">Add Awesome Title Here</div><div class="sub">ADD SUBTITLE HERE</div></div>
  <div class="abs" style="left:0;top:34px;width:386px;height:1px;background:var(--line)"></div>
  <div class="tab-b"></div><div class="foot-copy">Copyright © | All Rights Reserved</div><div class="foot-brand"><i></i>Medivant</div>
</section>

<!-- row 4 -->
<section class="slide c1" style="top:1190px">
  <div class="ph" style="left:0;top:0;width:228px;height:142px;border-radius:0 0 26px 0;background:linear-gradient(135deg,#1c2a44,#2f4f78)" role="img" aria-label="Photograph of code on a computer screen"></div>
  <div class="card" style="left:190px;top:46px;width:106px;height:80px;background:#8c6cc0">
    <div style="font-weight:700;font-size:10px;margin-bottom:4px">01.</div>
    <div class="h">Your Text Here</div>
    <p class="txt">Short note about this point and why it matters here.</p>
  </div>
  <div class="abs" style="left:24px;top:160px;font-family:'Raleway',sans-serif;font-size:21px;color:var(--ink)">Your <b style="font-family:Montserrat,sans-serif;color:var(--indigo);font-weight:700">Awesome</b> Text Here</div>
  <div class="foot-copy">Copyright © | All Rights Reserved</div><div class="foot-num">10</div><div class="foot-brand"><i></i>Medivant</div>
</section>

<section class="slide c2" style="top:1190px">
  <div class="ph" style="left:0;top:0;width:386px;height:110px;background:linear-gradient(180deg,#2b3a52,#8ea6c2)" role="img" aria-label="Photograph of light tubes in an abstract tunnel"></div>
  <div class="card" style="left:20px;top:70px;width:112px;height:62px;background:#7d59b4"><div class="h">Your Text Here</div><p class="txt">Short note about this highlight for the quarter.</p></div>
  <div class="card" style="left:139px;top:70px;width:112px;height:62px;background:var(--teal)"><div class="h">Your Text Here</div><p class="txt">Short note about this highlight for the quarter.</p></div>
  <div class="card" style="left:258px;top:70px;width:112px;height:62px;background:#6a7bcc"><div class="h">Your Text Here</div><p class="txt">Short note about this highlight for the quarter.</p></div>
  <div class="abs" style="left:0;top:142px;width:386px;text-align:center;font-family:'Raleway',sans-serif;font-size:15px">Company <b style="font-family:Montserrat,sans-serif;color:var(--violet);font-weight:600">Highlights</b></div>
  <p class="txt abs" style="left:18px;top:170px;width:350px;text-align:center">A short overview of the company results this year, with notes on growth, new partners and the next steps planned for the coming season.</p>
  <div class="foot-copy">Copyright © | All Rights Reserved</div><div class="foot-num">11</div><div class="foot-brand"><i></i>Medivant</div>
</section>

<section class="slide c3" style="top:1190px">
  <div class="tab"></div>
  <div class="head"><div class="ttl">Add Awesome Title Here</div><div class="sub">ADD SUBTITLE HERE</div></div>
  <div class="abs" style="left:20px;top:58px;width:346px">
    <p class="txt" style="margin-bottom:6px">Use this page for longer written content. Describe the context, the approach taken by the team and the main outcome in a few clear sentences that read easily.</p>
    <p class="txt" style="margin-bottom:6px">Add a second paragraph with supporting detail, such as data sources, review steps and the people who took part in the work across each region.</p>
    <p class="txt" style="margin-bottom:6px">A third paragraph can explain risks, open questions and the decisions still needed, so the audience knows what is expected of them next.</p>
    <p class="txt">Close with a short summary of the key message and the date of the next review meeting.</p>
  </div>
  <div class="tab-b"></div><div class="foot-copy">Copyright © | All Rights Reserved</div><div class="foot-num">9</div><div class="foot-brand"><i></i>Medivant</div>
</section>

<!-- row 5 -->
<section class="slide c1" style="top:1420px">
  <div class="tab"></div>
  <div class="head"><div class="ttl">Add Awesome Title Here</div><div class="sub">ADD SUBTITLE HERE</div></div>
  <div class="item" style="left:34px;top:66px"><i class="ico" style="border-radius:3px"></i><div><div class="nm">Project name</div><p class="txt">Short note on the goals and results of this project.</p></div></div>
  <div class="item" style="left:200px;top:66px"><i class="ico" style="border-radius:3px"></i><div><div class="nm">Project name</div><p class="txt">Short note on the goals and results of this project.</p></div></div>
  <div class="item" style="left:34px;top:106px"><i class="ico" style="border-radius:3px"></i><div><div class="nm">Project name</div><p class="txt">Short note on the goals and results of this project.</p></div></div>
  <div class="item" style="left:200px;top:106px"><i class="ico" style="border-radius:3px"></i><div><div class="nm">Project name</div><p class="txt">Short note on the goals and results of this project.</p></div></div>
  <div class="item" style="left:34px;top:146px"><i class="ico" style="border-radius:3px"></i><div><div class="nm">Project name</div><p class="txt">Short note on the goals and results of this project.</p></div></div>
  <div class="item" style="left:200px;top:146px"><i class="ico" style="border-radius:3px"></i><div><div class="nm">Project name</div><p class="txt">Short note on the goals and results of this project.</p></div></div>
  <div class="tab-b"></div><div class="foot-copy">Copyright © | All Rights Reserved</div><div class="foot-num">13</div><div class="foot-brand"><i></i>Medivant</div>
</section>

<section class="slide c2" style="top:1420px">
  <div class="ph" style="left:-5px;top:14px;width:152px;height:152px;border-radius:50%;border:4px solid var(--indigo);background:radial-gradient(circle,#3c7fd0,#12203f)" role="img" aria-label="Photograph of glowing blue network lines"></div>
  <div class="head left" style="left:168px;top:50px;width:200px"><div class="ttl">Add Awesome Title Here</div><div class="sub">ADD SUBTITLE HERE</div></div>
  <p class="txt abs" style="left:168px;top:80px;width:196px">Describe the project here in a few lines. Explain the goal, the method and the result the team reached, and what it means for the business over the next period.</p>
  <div class="item" style="left:168px;top:148px;width:100px"><i class="ico" style="background:var(--indigo)"></i><div><div class="nm">Project name</div><p class="txt">Short note on this project.</p></div></div>
  <div class="item" style="left:274px;top:148px;width:100px"><i class="ico" style="background:var(--indigo)"></i><div><div class="nm">Project name</div><p class="txt">Short note on this project.</p></div></div>
  <div class="tab-b"></div><div class="foot-copy">Copyright © | All Rights Reserved</div><div class="foot-num">14</div><div class="foot-brand"><i></i>Medivant</div>
</section>

<section class="slide c3" style="top:1420px">
  <div class="ph" style="left:8px;top:0;width:145px;height:216px;background:linear-gradient(160deg,#1e3c5f,#4d7d9e 50%,#c9d3dc)" role="img" aria-label="Photograph of a laptop on a desk"></div>
  <div class="head left" style="left:162px;top:38px;width:210px"><div class="ttl">Add Awesome Title Here</div><div class="sub">ADD SUBTITLE HERE</div></div>
  <p class="txt abs" style="left:162px;top:68px;width:200px">Short text explaining the main idea of this slide, the group it serves and the result it brings to the people who use it every day.</p>
  <div class="card" style="left:110px;top:118px;width:76px;height:78px;background:#8c6cc0;text-align:center"><div class="h" style="margin-top:14px">Project name</div><p class="txt">Short note on this project and its result.</p></div>
  <div class="card" style="left:192px;top:118px;width:76px;height:78px;background:#fff;border:1px solid var(--line);text-align:center"><div class="h" style="color:var(--ink);margin-top:14px">Project name</div><p class="txt" style="color:#60606c">Short note on this project and its result.</p></div>
  <div class="card" style="left:274px;top:118px;width:76px;height:78px;background:#fff;border:1px solid var(--line);text-align:center"><div class="h" style="color:var(--ink);margin-top:14px">Project name</div><p class="txt" style="color:#60606c">Short note on this project and its result.</p></div>
  <div class="foot-copy" style="left:180px">Copyright © | All Rights Reserved</div><div class="foot-brand"><i></i>Medivant</div>
</section>

<!-- row 6 -->
<section class="slide c1" style="top:1650px">
  <div class="head"><div class="ttl">Add Awesome Title Here</div><div class="sub">ADD SUBTITLE HERE</div></div>
  <svg class="abs" style="left:20px;top:60px" width="58" height="58"><circle cx="29" cy="29" r="24" fill="none" stroke="#e1e4f2" stroke-width="5"/><circle cx="29" cy="29" r="24" fill="none" stroke="var(--indigo)" stroke-width="5" pathLength="100" stroke-dasharray="45 100" transform="rotate(-90 29 29)"/></svg>
  <div class="donut-label" style="left:20px;top:82px;width:58px;font-size:11px;color:var(--indigo)">45%</div>
  <div class="abs" style="left:20px;top:126px;font-size:4.6px;font-weight:600">Your Text Here</div>
  <p class="txt abs" style="left:20px;top:134px;width:120px">You can add a short note here to explain the figure and its source.</p>
  <div class="ph" style="left:140px;top:42px;width:240px;height:155px;background:linear-gradient(180deg,#222,#444)" role="img" aria-label="Laptop showing a web search page"></div>
  <div class="abs" style="left:164px;top:48px;width:200px;height:130px;background:#fff;text-align:center;padding-top:42px">
    <div style="font-size:12px;font-weight:500;color:var(--indigo)">Seeker</div>
    <div style="margin:6px auto 0;width:96px;height:6px;border:1px solid #ccc;border-radius:3px"></div>
  </div>
  <div class="foot-copy">Copyright © | All Rights Reserved</div><div class="foot-num">16</div><div class="foot-brand"><i></i>Medivant</div>
</section>

<section class="slide c2" style="top:1650px">
  <div class="abs" style="left:0;top:22px;width:386px;height:76px;background:var(--grad-h);text-align:center;padding-top:14px"><div class="ttl" style="color:#fff;font-size:14px">Add Awesome Title Here</div><div class="sub" style="color:#e9ecff">ADD SUBTITLE HERE</div></div>
  <div class="abs" style="left:47px;top:84px;width:292px;display:flex;justify-content:space-between">
    <i style="width:28px;height:28px;border-radius:50%;background:#8c6cc0;border:2px solid #fff"></i>
    <i style="width:28px;height:28px;border-radius:50%;background:#8c6cc0;border:2px solid #fff"></i>
    <i style="width:28px;height:28px;border-radius:50%;background:#8c6cc0;border:2px solid #fff"></i>
    <i style="width:28px;height:28px;border-radius:50%;background:#8c6cc0;border:2px solid #fff"></i>
  </div>
  <div class="abs" style="left:25px;top:134px;width:336px;display:flex;justify-content:space-between;text-align:center">
    <div style="width:74px"><div style="font-size:5px;font-weight:700">Lorem ipsum dolor</div><p class="txt">Short note on this key value.</p></div>
    <div style="width:74px"><div style="font-size:5px;font-weight:700">Lorem ipsum dolor</div><p class="txt">Short note on this key value.</p></div>
    <div style="width:74px"><div style="font-size:5px;font-weight:700">Lorem ipsum dolor</div><p class="txt">Short note on this key value.</p></div>
    <div style="width:74px"><div style="font-size:5px;font-weight:700">Lorem ipsum dolor</div><p class="txt">Short note on this key value.</p></div>
  </div>
  <div class="tab-b"></div><div class="foot-copy">Copyright © | All Rights Reserved</div><div class="foot-num">17</div><div class="foot-brand"><i></i>Medivant</div>
</section>

<section class="slide c3" style="top:1650px">
  <div class="head"><div class="ttl">Add Awesome Title Here</div><div class="sub">ADD SUBTITLE HERE</div></div>
  <svg class="abs" style="left:50px;top:64px" width="110" height="110"><circle cx="55" cy="55" r="42" fill="none" stroke="#d9f3f7" stroke-width="14"/><circle cx="55" cy="55" r="42" fill="none" stroke="url(#g72)" stroke-width="14" pathLength="100" stroke-dasharray="72 100" transform="rotate(-90 55 55)"/><defs><linearGradient id="g72" x1="0" y1="0" x2="1" y2="1"><stop offset="0" stop-color="#1fc0d6"/><stop offset="1" stop-color="#6b449b"/></linearGradient></defs></svg>
  <div class="donut-label" style="left:50px;top:106px;width:110px;font-size:21px">72%</div>
  <div class="abs" style="left:194px;top:76px;width:170px">
    <div class="bul"><i></i><p class="txt">Short line on the first key result and what it shows.</p></div>
    <div class="bul"><i></i><p class="txt">Short line on the second key result and what it shows.</p></div>
    <div class="bul"><i></i><p class="txt">Short line on the third key result and what it shows.</p></div>
  </div>
  <div class="foot-copy">Copyright © | All Rights Reserved</div><div class="foot-num">15</div><div class="foot-brand"><i></i>Medivant</div>
</section>

<!-- row 7 -->
<section class="slide c1" style="top:1880px">
  <svg class="abs" style="left:0;top:0" width="386" height="216">
    <circle cx="90" cy="70" r="40" fill="none" stroke="#e3e5ef" stroke-width="9"/>
    <circle cx="90" cy="70" r="40" fill="none" stroke="var(--indigo)" stroke-width="9" pathLength="100" stroke-dasharray="85 100" transform="rotate(-90 90 70)"/>
    <circle cx="150" cy="118" r="33" fill="none" stroke="#e3e5ef" stroke-width="8"/>
    <circle cx="150" cy="118" r="33" fill="none" stroke="var(--violet)" stroke-width="8" pathLength="100" stroke-dasharray="60 100" transform="rotate(-90 150 118)"/>
    <circle cx="87" cy="145" r="26" fill="none" stroke="#e3e5ef" stroke-width="6"/>
    <circle cx="87" cy="145" r="26" fill="none" stroke="var(--teal)" stroke-width="6" pathLength="100" stroke-dasharray="35 100" transform="rotate(-90 87 145)"/>
  </svg>
  <div class="donut-label" style="left:60px;top:63px;width:60px;font-size:12px">85<small style="font-size:7px">%</small></div>
  <div class="donut-label" style="left:120px;top:111px;width:60px;font-size:12px">60<small style="font-size:7px">%</small></div>
  <div class="donut-label" style="left:57px;top:140px;width:60px;font-size:9px">35<small style="font-size:6px">%</small></div>
  <div class="abs" style="left:226px;top:52px;font-family:'Raleway',sans-serif;font-size:17px">Chart</div>
  <div class="abs" style="left:226px;top:72px;font-size:6px">Lorem ipsum dolor sit amet</div>
  <div class="abs" style="left:228px;top:92px;font-size:11px;font-weight:700;color:var(--indigo)">35 %</div>
  <p class="txt abs" style="left:262px;top:93px;width:110px">Short note that explains this value.</p>
  <p class="txt abs" style="left:228px;top:108px;width:140px">Add a short line to explain where this data comes from and how to read it.</p>
  <p class="txt abs" style="left:236px;top:128px;width:130px">First supporting point for this chart.</p>
  <p class="txt abs" style="left:236px;top:142px;width:130px">Second supporting point for this chart.</p>
  <div class="foot-copy">Copyright © | All Rights Reserved</div><div class="foot-num">19</div><div class="foot-brand"><i></i>Medivant</div>
</section>

<section class="slide c2" style="top:1880px">
  <div class="head"><div class="ttl">Add Awesome Title Here</div><div class="sub">ADD SUBTITLE HERE</div></div>
  <div class="abs" style="left:24px;top:60px;width:160px">
    <p class="txt" style="margin-bottom:6px">Use this column for the main written content. Describe the topic, the approach and the findings in clear sentences so the reader can follow along.</p>
    <p class="txt">Add more detail on method, timing and the people involved, and close with the key message that should be remembered after the meeting ends.</p>
  </div>
  <div class="card" style="left:194px;top:60px;width:166px;height:52px;background:#7d59b4;text-align:center;padding-top:12px"><p class="txt">A key message placed in a box so it stands out from the body text on the page.</p></div>
  <div class="card" style="left:194px;top:124px;width:166px;height:52px;background:var(--teal);text-align:center;padding-top:12px"><p class="txt">A key message placed in a box so it stands out from the body text on the page.</p></div>
  <div class="foot-copy">Copyright © | All Rights Reserved</div><div class="foot-num">20</div><div class="foot-brand"><i></i>Medivant</div>
</section>

<section class="slide c3" style="top:1880px">
  <div class="head"><div class="ttl">Add Awesome Title Here</div><div class="sub">ADD SUBTITLE HERE</div></div>
  <div class="abs" style="left:54px;top:66px;font-size:5px;line-height:22.6px">
    <div>Header Text Here <span style="color:var(--teal)">●</span></div>
    <div>Header Text Here <span style="color:var(--indigo)">●</span></div>
    <div>Header Text Here <span style="color:var(--indigo)">●</span></div>
    <div>Header Text Here <span style="color:var(--indigo)">●</span></div>
    <div>Header Text Here <span style="color:var(--indigo)">●</span></div>
  </div>
  <svg class="abs" style="left:180px;top:44px" width="150" height="150">
    <circle cx="75" cy="75" r="73" fill="#1fc0d6"/>
    <circle cx="75" cy="90" r="58" fill="#4b87cc"/>
    <circle cx="75" cy="104" r="44" fill="#5d6cc3"/>
    <circle cx="75" cy="117" r="31" fill="#6a58b2"/>
    <circle cx="75" cy="129" r="19" fill="#7b52b0"/>
  </svg>
  <div class="abs" style="left:180px;top:50px;width:150px;text-align:center;font-size:3.6px;color:#fff;line-height:1">
    <div>28.29 M</div><div style="margin-top:18px">20.29 M</div><div style="margin-top:20px">15.29 M</div><div style="margin-top:20px">8.29 M</div><div style="margin-top:20px">65.29 K</div>
  </div>
  <div class="foot-copy">Copyright © | All Rights Reserved</div><div class="foot-num">18</div><div class="foot-brand"><i></i>Medivant</div>
</section>

<!-- row 8 -->
<section class="slide c1" style="top:2110px">
  <div class="head left" style="left:30px;top:62px;width:180px"><div class="ttl">Add Awesome Title Here</div><div class="sub">ADD SUBTITLE HERE</div></div>
  <p class="txt abs" style="left:30px;top:96px;width:110px">Short text explaining the three funding values shown on the right side of this slide and how they grew.</p>
  <svg class="abs" style="left:0;top:0" width="386" height="216">
    <circle cx="316" cy="72" r="38" fill="var(--teal)"/>
    <circle cx="282" cy="123" r="30" fill="var(--violet)"/>
    <circle cx="248" cy="164" r="22" fill="var(--indigo)"/>
    <g stroke="#2a2a33" stroke-width=".5" fill="none"><path d="M250 48 H278"/><path d="M210 100 H252"/><path d="M175 140 H226"/></g>
  </svg>
  <div class="abs" style="left:278px;top:62px;width:76px;text-align:center;color:#fff;font-size:5.5px;font-weight:700">800.000 USD</div>
  <div class="abs" style="left:252px;top:115px;width:60px;text-align:center;color:#fff;font-size:5px;font-weight:700">4000 USD</div>
  <div class="abs" style="left:226px;top:158px;width:44px;text-align:center;color:#fff;font-size:4.6px;font-weight:700">3M USD</div>
  <p class="txt abs" style="left:200px;top:26px;width:50px">Short note on this value.</p>
  <p class="txt abs" style="left:160px;top:90px;width:50px">Short note on this value.</p>
  <p class="txt abs" style="left:124px;top:130px;width:50px">Short note on this value.</p>
  <div class="foot-copy">Copyright © | All Rights Reserved</div><div class="foot-num">22</div><div class="foot-brand"><i></i>Medivant</div>
</section>

<section class="slide c2" style="top:2110px">
  <div class="hdr"><div class="ttl">Add Awesome Title Here</div><div class="sub">ADD SUBTITLE HERE</div></div>
  <div class="tab"></div>
  <p class="txt abs" style="left:30px;top:70px;width:326px;text-align:center">A short line of context for the three figures below, explaining what was measured and over which period the data was collected.</p>
  <svg class="abs" style="left:0;top:0" width="386" height="216">
    <g fill="none" stroke-width="4"><circle cx="108" cy="132" r="24" stroke="#e3e5ef"/><circle cx="190" cy="132" r="24" stroke="#e3e5ef"/><circle cx="272" cy="132" r="24" stroke="#e3e5ef"/></g>
    <g fill="none" stroke-width="4"><circle cx="108" cy="132" r="24" stroke="var(--teal)" pathLength="100" stroke-dasharray="50 100" transform="rotate(-90 108 132)"/><circle cx="190" cy="132" r="24" stroke="var(--violet)" pathLength="100" stroke-dasharray="75 100" transform="rotate(-90 190 132)"/><circle cx="272" cy="132" r="24" stroke="var(--indigo)" pathLength="100" stroke-dasharray="40 100" transform="rotate(-90 272 132)"/></g>
  </svg>
  <div class="donut-label" style="left:78px;top:124px;width:60px;font-size:13px">50%</div>
  <div class="donut-label" style="left:160px;top:124px;width:60px;font-size:13px">75%</div>
  <div class="donut-label" style="left:242px;top:124px;width:60px;font-size:13px">40%</div>
  <p class="txt abs" style="left:80px;top:164px;width:56px;text-align:center">Short label for this value</p>
  <p class="txt abs" style="left:162px;top:164px;width:56px;text-align:center">Short label for this value</p>
  <p class="txt abs" style="left:244px;top:164px;width:56px;text-align:center">Short label for this value</p>
  <div class="foot-copy">Copyright © | All Rights Reserved</div><div class="foot-num">23</div><div class="foot-brand"><i></i>Medivant</div>
</section>

<section class="slide c3" style="top:2110px">
  <div class="ph" style="left:3px;top:0;width:160px;height:216px;background:linear-gradient(180deg,#0f4f8a,#2eb5e0 70%,#0e2a48)" role="img" aria-label="Photograph of a blue robotic hand"></div>
  <div class="card" style="left:30px;top:128px;width:66px;height:66px;background:var(--teal);text-align:center;padding:8px 4px"><div style="font-size:10px;font-weight:700">7,500+</div><div style="font-size:4.6px">Your Stats</div><p class="txt">Short note on this stat.</p></div>
  <div class="card" style="left:98px;top:110px;width:70px;height:84px;background:var(--violet);text-align:center;padding:20px 4px"><div style="font-size:10px;font-weight:700">6,000+</div><div style="font-size:4.6px">Your Text</div><p class="txt">Short note on this stat.</p></div>
  <div class="head left" style="left:198px;top:30px;width:180px"><div class="ttl">Add Awesome Title Here</div><div class="sub">ADD SUBTITLE HERE</div></div>
  <p class="txt abs" style="left:198px;top:60px;width:170px">Short text about the two stats on the left and the work behind them over the past year.</p>
  <div class="abs" style="left:190px;top:104px;width:180px">
    <div class="bul"><i></i><p class="txt">First point on this topic in one or two short lines.</p></div>
    <div class="bul"><i></i><p class="txt">Second point on this topic in one or two short lines.</p></div>
    <div class="bul"><i></i><p class="txt">Third point on this topic in one or two short lines.</p></div>
  </div>
  <div class="foot-num" style="left:190px">21</div><div class="foot-brand"><i></i>Medivant</div>
</section>

<!-- row 9 -->
<section class="slide c1" style="top:2340px">
  <div class="tab"></div>
  <div class="head"><div class="ttl">Add Awesome Title Here</div><div class="sub">ADD SUBTITLE HERE</div></div>
  <div class="abs" style="left:30px;top:66px;width:326px;display:flex;justify-content:space-between;text-align:center">
    <div style="width:66px"><div role="img" aria-label="Portrait photograph of a team member" style="width:38px;height:38px;margin:0 auto 6px;border-radius:50%;background:#c9cde0"></div><div style="font-size:4.6px;font-weight:700;color:var(--indigo)">YOUR NAME</div><div style="font-size:5px">CEO and Director</div><p class="txt">Short note about this person and role.</p></div>
    <div style="width:66px"><div role="img" aria-label="Portrait photograph of a team member" style="width:38px;height:38px;margin:0 auto 6px;border-radius:50%;background:#c9cde0"></div><div style="font-size:4.6px;font-weight:700;color:var(--indigo)">YOUR NAME</div><div style="font-size:5px">CEO and Director</div><p class="txt">Short note about this person and role.</p></div>
    <div style="width:66px"><div role="img" aria-label="Portrait photograph of a team member" style="width:38px;height:38px;margin:0 auto 6px;border-radius:50%;background:#c9cde0"></div><div style="font-size:4.6px;font-weight:700;color:var(--indigo)">YOUR NAME</div><div style="font-size:5px">CEO and Director</div><p class="txt">Short note about this person and role.</p></div>
    <div style="width:66px"><div role="img" aria-label="Portrait photograph of a team member" style="width:38px;height:38px;margin:0 auto 6px;border-radius:50%;background:#c9cde0"></div><div style="font-size:4.6px;font-weight:700;color:var(--indigo)">YOUR NAME</div><div style="font-size:5px">CEO and Director</div><p class="txt">Short note about this person and role.</p></div>
  </div>
  <div class="tab-b"></div><div class="foot-copy">Copyright © | All Rights Reserved</div><div class="foot-num">25</div><div class="foot-brand"><i></i>Medivant</div>
</section>

<section class="slide c2" style="top:2340px">
  <div class="ph" style="inset:0;background:linear-gradient(135deg,#d7d9e0,#f1f2f6 60%,#c9ccd6)" role="img" aria-label="Faint photograph of glass building architecture"></div>
  <div class="abs" style="left:18px;top:18px;width:350px;height:180px;background:#fff;border-radius:14px"></div>
  <div class="abs" style="left:52px;top:42px;width:104px;height:134px;background:#fff;box-shadow:0 3px 10px rgba(0,0,0,.12)">
    <div style="background:var(--indigo);height:22px;color:#fff;font-size:4.4px;display:flex;align-items:center;gap:6px;padding-left:8px"><i style="width:6px;height:6px;border:1px solid #fff;border-radius:50%"></i>www.medivant.co</div>
    <div style="padding:6px 8px;font-size:4.2px;line-height:1.4;color:#555">
      <div style="display:flex;gap:8px;margin-bottom:10px"><svg width="6" height="8" viewBox="0 0 6 8"><path d="M3 8 C1 5 0 4 0 3 A3 3 0 0 1 6 3 C6 4 5 5 3 8Z" fill="var(--indigo)"/></svg><span>Here to write your<br>company address</span></div>
      <div style="display:flex;gap:8px;margin-bottom:12px"><svg width="7" height="7" viewBox="0 0 7 7"><path d="M1 0 L3 2 L2 3 Q3 5 4 5 L5 4 L7 6 L6 7 Q0 7 0 1Z" fill="var(--indigo)"/></svg><span>(555) 010-2024</span></div>
      <div style="display:flex;gap:8px"><svg width="8" height="6" viewBox="0 0 8 6"><rect width="8" height="6" fill="var(--indigo)"/><path d="M0 0 L4 3 L8 0" stroke="#fff" stroke-width=".8" fill="none"/></svg><span>info@medivant.co</span></div>
    </div>
    <div class="socials" style="color:var(--indigo);margin-top:10px"><i></i><i></i><i></i><i></i></div>
  </div>
  <div class="abs brand" style="left:200px;top:94px;font-size:22px"><i style="width:24px;height:24px"></i>Medivant</div>
</section>

<section class="slide c3" style="top:2340px">
  <div class="ph" style="left:0;top:0;width:82px;height:216px;background:linear-gradient(180deg,#8e8f96 0%,#b9bac0 55%,#a3a4ab 100%)" role="img" aria-label="Aerial photograph of people crossing a pedestrian crossing"></div>
  <div class="abs" style="left:82px;top:0;width:40px;height:216px;background:var(--violet)"></div>
  <div class="abs" style="left:66px;top:92px;width:72px;transform:rotate(-90deg);font-weight:700;font-size:10px;color:#fff;white-space:nowrap;text-align:center">Table of Content</div>
  <div class="abs" style="left:205px;top:36px;font-size:5.5px;line-height:20.6px">
    <div><b>01</b>&nbsp; Add your content here</div>
    <div><b>02</b>&nbsp; Add your content here</div>
    <div><b>03</b>&nbsp; Add your content here</div>
    <div><b>04</b>&nbsp; Add your content here</div>
    <div><b>05</b>&nbsp; Add your content here</div>
    <div><b>06</b>&nbsp; Add your content here</div>
    <div><b>07</b>&nbsp; Add your content here</div>
  </div>
  <div class="foot-num" style="left:130px">24</div><div class="foot-brand"><i></i>Medivant</div>
</section>

</div>
</body>
</html>
```